Grandpa Turnip's Valley Harvest Delivery

Two-sided postcard.

Front side: Can be a photo of available products. Need at least a 2" x 4" space to speak to the recipient and let them know who the post card is for and who it is from.

Back side: We will apply a sticker for the delivery address and space should be included for stamp.

```html
<!DOCTYPE html>
<html lang="en">
<head>
<meta charset="utf-8">
<title>Grandpa Turnip's Valley Harvest Delivery – Postcard</title>
<link href="https://fonts.googleapis.com/css2?family=Montserrat:wght@400;500;600;700;800&display=swap" rel="stylesheet">
<style>
  :root{
    --green:#1f8a3e;
    --green-dark:#1a6e34;
    --yellow:#ebe521;
    --white:#ffffff;
    --ink:#2b2b2b;
    --stage:#3a3a3a;
  }
  *{box-sizing:border-box;margin:0;padding:0}
  html,body{width:1200px;height:546px;overflow:hidden;background:var(--stage);font-family:'Montserrat',sans-serif}
  .canvas{position:relative;width:1200px;height:546px}
  .card{position:absolute;top:103px;width:498px;height:338px;overflow:hidden;background:var(--white)}
  .card--front{left:68px}
  .card--back{left:639px}
  .card svg.shapes{position:absolute;inset:0;width:100%;height:100%}

  .brand-name{position:absolute;left:14px;top:36px;display:flex;align-items:center;gap:6px;
    color:var(--green);font-weight:700;font-size:14px;line-height:1.15}
  .brand-name .dot{width:10px;height:10px;border-radius:50%;background:var(--green);flex:none}

  .headline{position:absolute;left:35px;top:200px;font-weight:800;line-height:.9}
  .headline .free{display:block;color:var(--white);font-size:35px}
  .headline .box{display:block;color:var(--yellow);font-size:49px}
  .offer{position:absolute;left:37px;top:276px;color:var(--white);font-size:13px;line-height:17px;font-weight:500;letter-spacing:.2px}
  .offer strong{color:var(--yellow);font-weight:700}

  .discount{position:absolute;left:364px;top:58px;width:80px;text-align:center;color:var(--ink);font-weight:700;line-height:1}
  .discount .label{display:block;font-size:11px;font-weight:600}
  .discount .value{display:block;font-size:24px;font-weight:800}

  .section-title{position:absolute;left:39px;color:var(--yellow);font-weight:700;font-size:16.5px;line-height:1}
  .title-about{top:20px}
  .title-services{top:148px}
  .about-text{position:absolute;left:39px;top:41px;width:204px;color:var(--white);font-size:8px;line-height:11px}
  .service-list{list-style:none}
  .service-item{position:absolute;left:39px;width:200px;padding-left:21px;color:var(--white);font-size:8px;line-height:10.5px}
  .service-item::before{content:"";position:absolute;left:0;top:1px;width:11px;height:11px;background:var(--white)}
  .service-item.accent::before{background:var(--yellow)}

  .call{position:absolute;left:0;width:260px;top:283px;text-align:center;color:var(--ink)}
  .call svg{width:22px;height:22px;display:block;margin:0 auto 5px}
  .call span{font-size:11.5px;font-weight:500}

  .stamp-box{position:absolute;left:382px;top:38px;width:78px;height:78px;border:1px solid var(--ink)}
  .address-line{position:absolute;left:278px;width:182px;border-top:1px solid var(--ink)}
</style>
</head>
<body>
<div class="canvas">

  <section class="card card--front" aria-label="Postcard front">
    <svg class="shapes" viewBox="0 0 498 338">
      <defs>
        <linearGradient id="produceTones" x1="0" y1="0" x2="1" y2="1">
          <stop offset="0" stop-color="#8e9a6a"/>
          <stop offset=".45" stop-color="#c46a3e"/>
          <stop offset="1" stop-color="#3f6b2e"/>
        </linearGradient>
        <linearGradient id="dairyTones" x1="0" y1="0" x2="1" y2="1">
          <stop offset="0" stop-color="#f4f1ec"/>
          <stop offset="1" stop-color="#d9a377"/>
        </linearGradient>
      </defs>
      <polygon points="189,0 498,0 498,99 290,338 0,338 0,218" fill="var(--green)"/>
      <path d="M0,218 C40,180 120,175 180,210 C245,248 262,290 265,338 L0,338 Z" fill="var(--green-dark)"/>
      <polygon points="283,20 394,84 394,212 283,276 172,212 172,84" fill="var(--yellow)" stroke="var(--yellow)" stroke-width="14" stroke-linejoin="round"/>
      <polygon role="img" aria-label="Photo of a box of fresh local produce: vegetables, fruit, eggs and milk" points="283,30 385,89 385,207 283,266 181,207 181,89" fill="url(#produceTones)" stroke="url(#produceTones)" stroke-width="10" stroke-linejoin="round"/>
      <polygon points="397,174 465,213 465,291 397,330 329,291 329,213" fill="var(--yellow)" stroke="var(--yellow)" stroke-width="12" stroke-linejoin="round"/>
      <polygon role="img" aria-label="Photo of milk bottle, glass of milk and a bowl of eggs" points="397,182 458,217 458,287 397,322 336,287 336,217" fill="url(#dairyTones)" stroke="url(#dairyTones)" stroke-width="8" stroke-linejoin="round"/>
      <polygon points="404,34 440,55 440,97 404,118 368,97 368,55" fill="var(--yellow)" stroke="var(--yellow)" stroke-width="14" stroke-linejoin="round"/>
      <g stroke="var(--white)" stroke-width="2" stroke-linecap="round">
        <path d="M392,8 l6,6 M398,8 l-6,6"/>
        <path d="M191,32 l6,6 M197,32 l-6,6"/>
        <path d="M479,314 l6,6 M485,314 l-6,6" stroke="var(--ink)"/>
        <path d="M33,116 l6,6 M39,116 l-6,6" stroke="var(--ink)"/>
      </g>
      <circle cx="438" cy="143" r="4.5" fill="none" stroke="var(--white)" stroke-width="2"/>
      <circle cx="181" cy="320" r="4.5" fill="none" stroke="var(--white)" stroke-width="2"/>
    </svg>

    <div class="brand-name"><span class="dot"></span><span>Grandpa Turnip's</span></div>

    <div class="discount"><span class="label">DISCOUNT</span><span class="value">30%</span></div>

    <h1 class="headline"><span class="free">FREE</span><span class="box">BOX!</span></h1>
    <p class="offer">Enjoy your first box from<br>Grandpa Turnip's for <strong>FREE!</strong></p>
  </section>

  <section class="card card--back" aria-label="Postcard back">
    <svg class="shapes" viewBox="0 0 498 338">
      <rect x="0" y="0" width="260" height="338" fill="var(--green)"/>
      <path d="M0,235 C60,185 150,175 210,130 C240,110 255,85 260,75 L260,338 L0,338 Z" fill="var(--green-dark)"/>
      <path d="M0,322 L95,268 C118,255 142,255 165,268 L260,322 L260,338 L0,338 Z" fill="var(--yellow)"/>
    </svg>

    <h2 class="section-title title-about">ABOUT US</h2>
    <p class="about-text">Grandpa Turnip's is a farm to fork delivery service, working to bring the valley food landscape to your front door! Since 2008 we have been expanding our network of local growers and food artisans, and offer over 200 food products a week, and we are still growing! Our goal is to improve access to local foods in our community through transparency, communication, affordability, and the convenience of our delivery.</p>

    <h2 class="section-title title-services">OUR SERVICES</h2>
    <ul class="service-list">
      <li class="service-item" style="top:176px">Lorem ipsum dolor sit amet, consectetur adipiscing elit sed do.</li>
      <li class="service-item accent" style="top:204px">Lorem ipsum dolor sit amet, consectetur adipiscing elit sed do.</li>
      <li class="service-item" style="top:233px">Lorem ipsum dolor sit amet, consectetur adipiscing elit sed do.</li>
    </ul>

    <div class="call">
      <svg viewBox="0 0 24 24" aria-hidden="true"><path fill="var(--green)" d="M6.6 10.8a15.1 15.1 0 0 0 6.6 6.6l2.2-2.2a1 1 0 0 1 1-.25 11.4 11.4 0 0 0 3.6.57 1 1 0 0 1 1 1V20a1 1 0 0 1-1 1A17 17 0 0 1 3 4a1 1 0 0 1 1-1h3.5a1 1 0 0 1 1 1c0 1.25.2 2.45.57 3.57a1 1 0 0 1-.25 1z"/></svg>
      <span>CALL US:(00)015-7788-4120</span>
    </div>

    <div class="stamp-box" aria-label="Stamp area"></div>
    <div class="address-line" style="top:171px"></div>
    <div class="address-line" style="top:213px"></div>
    <div class="address-line" style="top:255px"></div>
    <div class="address-line" style="top:297px"></div>
  </section>

</div>
</body>
</html>
```